Real Estate Flyer (Brenton Property)

We need a color CMYK high resolution, print quality horizontal real estate property flyer designed in the sizes of 10" wide and 6.7425" tall and another one in 11" wide and 8.5" tall.
Ad should be professionally looking to U.S. standards. It should be sleek, modern yet classy.
We uploaded in Briefs logo files, agent photo, 2 photos of the property (Must use both) and a sample of a flyer for Vayle Morrow Luxury Residence. We like how the overlay atop the first photo in the Vayle Morrow flyer with the company logo in the overlay. We'd like to incorporate that with our logo, the background color of the overlay should match that of our logo. DON'T CHANGE LOGO COLORS. Only use two colors in ad (exact logo blue color and white). The text in the overlay must be "FOR SALE - Potential Income Producing Commercial Office Building". Other details that should be prominent underneath are "42 Brenton Dr., Schaumburg, IL 60174 - Asking Price: $650,000".
Add "Residential & Commercial" under our company logo in italic font.
Add in flyer: "Located seconds away from the Kettering Rd. & Palden Rd. Intersection"
Add in flyer:
- Completely vacant
- 10,000 sq. ft. building
- 55 Car Parking
- 1.38 acre lot
- Over 20 offices and 5 bathrooms.
- Lease out individual office spaces for great monthly cash flow
Put agent's photo and following details professionally displayed:
Dev Marlo
Managing Broker
847-555-0148
dev.marlo@qtnhomes-example.com
Add from Briefs fair housing logo and PLX logo near agent's information. Logos should be small but yet visible to understand text.
Add at bottom of the ad with separation near agent details:
Looking to Buy or Sell?
I’m your one-stop, full service licensed real estate broker.
I deal with all types of real estate properties: Homes, Condos, Townhomes, Multi-Unit Apartment Buildings and Commercial Spaces.
Let My Experience Guide You Through Every Step of the Process!
Fine print:
©2018 QTN Homes, Inc. All Rights Reserved.

```html
<!DOCTYPE html>
<html lang="en">
<head>
<meta charset="utf-8">
<title>Brenton Property – For Sale Flyer</title>
<link href="https://fonts.googleapis.com/css2?family=Poppins:ital,wght@0,300;0,400;0,500;0,600;0,700;1,400&display=swap" rel="stylesheet">
<style>
  :root{
    --brand-blue:#1c4bb0;
    --brand-blue-panel:#2246b3;
    --text-blue:#1b48ad;
    --check-navy:#16378f;
    --white:#ffffff;
    --photo-warm:#e4d3b8;
    --photo-asphalt:#3e4147;
  }
  *{margin:0;padding:0;box-sizing:border-box}
  html,body{width:1200px;height:933px;overflow:hidden;background:var(--white)}
  body{font-family:'Poppins',sans-serif;color:var(--text-blue)}
  .flyer{position:relative;width:1200px;height:933px;overflow:hidden;background:var(--white)}
  .abs{position:absolute}

  /* photography placeholders */
  .photo-main{left:0;top:0;width:857px;height:641px;
    background:linear-gradient(180deg,#9fb6cc 0%,#c8cfd2 28%,var(--photo-warm) 48%,#d8d3c8 62%,#6b6a64 78%,var(--photo-asphalt) 100%)}
  .photo-lot{left:865px;top:0;width:335px;height:176px;
    background:linear-gradient(180deg,#9aa88a 0%,#7e8a72 22%,#4c4f55 40%,var(--photo-asphalt) 100%)}
  .photo-row{left:865px;top:186px;width:335px;height:188px;
    background:linear-gradient(180deg,#a9b8c6 0%,#d9cdb8 40%,#c9c3b6 56%,#54565b 72%,var(--photo-asphalt) 100%)}

  /* contact block */
  .contact-phone{right:370px;top:14px;font-size:33px;font-weight:700;color:var(--text-blue);letter-spacing:.5px;display:flex;align-items:center;gap:6px}
  .contact-email{right:370px;top:63px;font-size:14.5px;font-weight:500;color:var(--text-blue);display:flex;align-items:center;gap:9px;white-space:nowrap}

  /* for-sale overlay */
  .overlay{left:0;top:0;width:857px;height:641px}
  .sale-title{left:25px;top:475px;font-size:50px;font-weight:600;color:var(--white);letter-spacing:-.5px}
  .sale-sub{left:25px;top:542px;font-size:21px;font-weight:300;color:var(--white)}
  .sale-address{left:25px;top:603px;font-size:18px;font-weight:500;color:var(--white)}

  /* location & features */
  .location{left:25px;top:650px;font-size:23px;font-weight:500;line-height:30px;color:var(--text-blue)}
  .location-rule{left:25px;top:722px;width:505px;height:2px;background:var(--text-blue)}
  .feature{display:flex;align-items:center;gap:26px;font-size:15.5px;font-weight:500;color:var(--text-blue);line-height:21px;white-space:nowrap}
  .feature svg{flex:none}

  /* brand block */
  .brand-box{left:632px;top:641px;width:225px;height:197px;background:var(--brand-blue);border-bottom-left-radius:80px;
    display:flex;flex-direction:column;align-items:center;justify-content:center;gap:8px;padding-top:6px;padding-left:10px}
  .brand-name{display:flex;align-items:center;gap:10px;font-size:29px;font-weight:600;color:var(--white);letter-spacing:.5px}
  .brand-name .mark{width:16px;height:16px;background:var(--white)}
  .brand-tag{font-size:12px;font-style:italic;font-weight:400;color:var(--white)}
  .badges{left:726px;top:867px;display:flex;gap:8px;align-items:flex-end}
  .badge{background:#1e2a44}
  .fine-print{left:688px;top:904px;width:162px;font-size:7px;text-align:right;color:var(--text-blue)}

  /* agent */
  .agent-panel{left:865px;top:374px;width:335px;height:265px;background:var(--brand-blue)}
  .agent-photo{left:943px;top:391px;width:168px;height:168px;border-radius:50%;border:4px solid var(--white);
    background:radial-gradient(circle at 50% 40%,#d8dde3 0%,#b8bfc8 55%,#2a2c33 100%)}
  .agent-name{left:865px;top:557px;width:335px;text-align:center;font-size:33px;font-weight:600;color:var(--white)}
  .agent-title{left:865px;top:600px;width:335px;text-align:center;font-size:13px;font-weight:300;color:var(--white)}

  /* pitch */
  .pitch-panel{left:865px;top:641px;width:335px;height:292px;background:var(--brand-blue-panel)}
  .pitch-title{left:865px;top:667px;width:335px;text-align:center;font-size:25px;font-weight:500;color:var(--white)}
  .pitch-lead{left:865px;top:711px;width:335px;text-align:center;font-size:15px;font-weight:600;line-height:21px;color:var(--white)}
  .pitch-rule{left:913px;top:770px;width:259px;height:2px;background:var(--white)}
  .pitch-deal{left:865px;top:786px;width:335px;text-align:center;font-size:17px;font-weight:300;line-height:22px;color:var(--white)}
  .pitch-types{left:865px;top:839px;width:335px;text-align:center;font-size:16px;font-weight:300;line-height:21px;color:var(--white)}

  .gutter{left:857px;top:0;width:8px;height:933px;background:var(--white)}
</style>
</head>
<body>
<main class="flyer">
  <div class="abs photo-main" role="img" aria-label="Photo of the two-storey white office building with dormer windows, trees and parked cars at sunset"></div>
  <div class="abs photo-lot" role="img" aria-label="Photo of the parking lot with accessible parking space"></div>
  <div class="abs photo-row" role="img" aria-label="Photo of the office building row seen across the parking lot"></div>
  <div class="abs gutter"></div>

  <div class="abs contact-phone">
    <svg width="26" height="30" viewBox="0 0 24 28" aria-hidden="true"><path d="M6 3c1-1 2-1 3 0l2 4c.5 1 .2 2-.6 2.6L9 10.8c1 3 3 5.5 5.6 7.2l1.4-1.2c.8-.7 2-.7 2.7.1l3 3c.8.8.8 2-.1 2.8l-1.6 1.5C17 27 5 17 4.3 6.6 4.2 5.3 5 4 6 3z" fill="var(--text-blue)"/><path d="M15 3a8 8 0 0 1 7 7M15 7a4 4 0 0 1 3 3" stroke="var(--text-blue)" stroke-width="1.6" fill="none"/></svg>
    847-555-0148
  </div>
  <div class="abs contact-email">
    <svg width="19" height="15" viewBox="0 0 20 16" aria-hidden="true"><rect x="1" y="2" width="18" height="13" rx="2" fill="var(--text-blue)"/><path d="M2 3l8 6 8-6" stroke="var(--white)" stroke-width="1.5" fill="none"/></svg>
    dev.marlo@qtnhomes-example.com
  </div>

  <svg class="abs overlay" viewBox="0 0 857 641" aria-hidden="true">
    <path d="M0 458 L500 458 C560 458 600 490 632 545 L632 641 L0 641 Z" fill="var(--brand-blue)" opacity=".92"/>
    <rect x="0" y="591" width="632" height="50" fill="#2a3f9e"/>
  </svg>
  <div class="abs sale-title">FOR SALE</div>
  <div class="abs sale-sub">Potential Income Producing Commercial Office Building</div>
  <div class="abs sale-address">42 Brenton Dr., Schaumburg, IL 60174 - Asking Price: $650,000</div>

  <div class="abs location">Located seconds away from the Kettering Rd. &amp;<br>Palden Rd. Intersection</div>
  <div class="abs location-rule"></div>

  <div class="abs feature" style="left:22px;top:743px">
    <svg width="32" height="32" viewBox="0 0 32 32" aria-hidden="true"><circle cx="16" cy="16" r="15" fill="var(--check-navy)"/><path d="M9 16.5l5 5 9-10" stroke="var(--white)" stroke-width="3" fill="none" stroke-linecap="round" stroke-linejoin="round"/></svg>
    Completely Vacant
  </div>
  <div class="abs feature" style="left:22px;top:806px">
    <svg width="32" height="32" viewBox="0 0 32 32" aria-hidden="true"><circle cx="16" cy="16" r="15" fill="var(--check-navy)"/><path d="M9 16.5l5 5 9-10" stroke="var(--white)" stroke-width="3" fill="none" stroke-linecap="round" stroke-linejoin="round"/></svg>
    10,000 Sq. Ft. Building
  </div>
  <div class="abs feature" style="left:22px;top:869px">
    <svg width="32" height="32" viewBox="0 0 32 32" aria-hidden="true"><circle cx="16" cy="16" r="15" fill="var(--check-navy)"/><path d="M9 16.5l5 5 9-10" stroke="var(--white)" stroke-width="3" fill="none" stroke-linecap="round" stroke-linejoin="round"/></svg>
    55 Car Parking
  </div>
  <div class="abs feature" style="left:317px;top:743px">
    <svg width="32" height="32" viewBox="0 0 32 32" aria-hidden="true"><circle cx="16" cy="16" r="15" fill="var(--check-navy)"/><path d="M9 16.5l5 5 9-10" stroke="var(--white)" stroke-width="3" fill="none" stroke-linecap="round" stroke-linejoin="round"/></svg>
    1.38 Acre Lot
  </div>
  <div class="abs feature" style="left:317px;top:806px">
    <svg width="32" height="32" viewBox="0 0 32 32" aria-hidden="true"><circle cx="16" cy="16" r="15" fill="var(--check-navy)"/><path d="M9 16.5l5 5 9-10" stroke="var(--white)" stroke-width="3" fill="none" stroke-linecap="round" stroke-linejoin="round"/></svg>
    Over 20 Offices and 5 Bathrooms
  </div>
  <div class="abs feature" style="left:317px;top:864px">
    <svg width="32" height="32" viewBox="0 0 32 32" aria-hidden="true"><circle cx="16" cy="16" r="15" fill="var(--check-navy)"/><path d="M9 16.5l5 5 9-10" stroke="var(--white)" stroke-width="3" fill="none" stroke-linecap="round" stroke-linejoin="round"/></svg>
    Lease Out Individual Office Spaces<br>For Great Monthly Cash Flow
  </div>

  <div class="abs brand-box">
    <div class="brand-name"><span class="mark"></span>QTN Homes</div>
    <div class="brand-tag">Residential &amp; Commercial</div>
  </div>
  <div class="abs badges" aria-label="Listing and fair housing badges">
    <span class="badge" style="width:30px;height:30px"></span>
    <span class="badge" style="width:38px;height:22px"></span>
    <span class="badge" style="width:28px;height:28px"></span>
  </div>
  <div class="abs fine-print">©2018 QTN Homes, Inc. All Rights Reserved.</div>

  <div class="abs agent-panel"></div>
  <div class="abs agent-photo" role="img" aria-label="Portrait photo of the managing broker"></div>
  <div class="abs agent-name">Dev Marlo</div>
  <div class="abs agent-title">Managing Broker</div>

  <div class="abs pitch-panel"></div>
  <div class="abs pitch-title">Looking to Buy or Sell?</div>
  <div class="abs pitch-lead">I’m your one-stop, full service<br>licensed real estate broker.</div>
  <div class="abs pitch-rule"></div>
  <div class="abs pitch-deal">I deal with all types of<br>real estate properties:</div>
  <div class="abs pitch-types">Homes, Condos, Townhomes,<br>Multi-Unit Apartment Buildings<br>and Commercial Spaces.</div>
</main>
</body>
</html>
```